Marriage Podcast Needs Cover Art

The name of the marriage podcast is "Lanterns at Dusk", representing a bond between the husband, wife, and God. The artwork needs to include a rope tied in a heart shape and the podcast name (Lanterns at Dusk). I prefer a simple background, but a subtle pattern would be okay too. In general, simplicity is better. The artwork should be easy on the eyes. This cover art is what my listeners will see in their podcast app next to each episode name. The image is small, so the text needs to be large enough to read in this context. This means there will not be enough room for large pockets of blank space. The design basically fills the entire canvas.

Please see the attachment for some suggestions. Thanks! :)

Target Market(s)

Young married couples

Industry/Entity Type

Rope

Requirements
Must have
• - Rope tied in a heart shape.
• - Text: "Lanterns at Dusk"
• - 1400 x 1400 pixels
Nice to have
• - Bright or warm colors that convey love/marriage
• - 3000 x 3000 pixels
Should not have
• Dark or muted-color background

```html
<!DOCTYPE html>
<html lang="en">
<head>
<meta charset="utf-8">
<title>Lanterns at Dusk — Podcast Cover</title>
<link rel="stylesheet" href="https://fonts.googleapis.com/css2?family=Montserrat:wght@700&display=swap">
<style>
  :root {
    --sky-light: #eef5fd;
    --sky-mid: #dcebfb;
    --sky-deep: #b3d3f7;
    --rope-tan: #c99d6c;
    --rope-shade: #a7784b;
    --title-brown: #5c3714;
  }
  html, body {
    margin: 0;
    padding: 0;
    overflow: hidden;
  }
  .cover {
    position: relative;
    width: 1200px;
    height: 1200px;
    overflow: hidden;
    background: linear-gradient(170deg, var(--sky-light) 0%, var(--sky-mid) 55%, var(--sky-deep) 100%);
  }
  .rope-heart {
    position: absolute;
    left: 0;
    top: 0;
    width: 1200px;
    height: 1200px;
  }
  .podcast-title {
    position: absolute;
    left: 0;
    right: 0;
    top: 370px;
    margin: 0;
    text-align: center;
    font-family: "Montserrat", sans-serif;
    font-weight: 700;
    color: var(--title-brown);
    line-height: 1;
  }
  .podcast-title span {
    display: block;
  }
  .title-main {
    font-size: 112px;
    letter-spacing: 0.12em;
    margin-right: -0.12em;
  }
  .title-link {
    font-size: 96px;
    letter-spacing: 0.1em;
    margin: 22px -0.1em 22px 0;
  }
  .title-end {
    font-size: 140px;
    letter-spacing: 0.14em;
    margin-right: -0.14em;
  }
</style>
</head>
<body>
  <main class="cover">
    <svg class="rope-heart" viewBox="0 0 1200 1200" role="img" aria-label="Rope tied into a heart shape with a loop knot at the top and crossed ends running off both sides">
      <defs>
        <linearGradient id="ropeTone" x1="0" y1="0" x2="0" y2="1">
          <stop offset="0" stop-color="var(--rope-tan)" stop-opacity="0.28"/>
          <stop offset="1" stop-color="var(--rope-shade)" stop-opacity="0.22"/>
        </linearGradient>
      </defs>
      <path d="M600 210 C520 40 300 20 180 80 C60 140 40 320 80 470 C140 700 380 900 600 1020 C820 900 1060 700 1120 470 C1160 320 1140 140 1020 80 C900 20 680 40 600 210 Z" fill="url(#ropeTone)"/>
    </svg>
    <h1 class="podcast-title">
      <span class="title-main">LANTERNS</span>
      <span class="title-link">AT</span>
      <span class="title-end">DUSK</span>
    </h1>
  </main>
</body>
</html>
```